Discreet simple classy for adult entertainment

I would like a matte black business card with gold writing for my business. Keeping it simple. Having my following:

Lana frost
Events. Entertainment. Promotions
0491726580

or alternatively could have what i had on my previous card below but i think i prefer the above as again - discretion.

Maybe a nice gold line thru the card or some other very simple design . Or not open to ideas/ can be doublesided if any good ideas with that.

included pics of my old bus card. not sure weather i want a photo on it or not. if i do it wont be the same pic. i kinda wanted a card that was discreet so if it was in someones wallet they wouldn't neccessarily realise it was from a stripper.

Target Market(s)

men

Industry/Entity Type

Business

Contact Information for Business Card

Lana frost
0491726580

Requirements
Nice to have
• i don't know i am really open to anything. im giving my cards to guys so something they can have in their wallet that is discreet preferably.

```html
<!DOCTYPE html>
<html lang="en">
<head>
<meta charset="utf-8">
<title>Lana Frost — Business Card</title>
<link href="https://fonts.googleapis.com/css2?family=Poppins:wght@400;700&family=Libre+Franklin:wght@400&display=swap" rel="stylesheet">
<style>
  :root {
    --backdrop: #9a9a9a;
    --card: #232325;
    --gold-light: #f0c45a;
    --gold-mid: #d4992b;
    --gold-deep: #a9741a;
    --silver: #e4e4e4;
  }
  * { box-sizing: border-box; margin: 0; padding: 0; }
  html, body {
    width: 1200px;
    height: 1200px;
    overflow: hidden;
    background: var(--backdrop);
  }
  .sheet {
    width: 1200px;
    height: 1200px;
    display: flex;
    flex-direction: column;
    align-items: center;
    justify-content: center;
    gap: 40px;
  }
  .card {
    position: relative;
    width: 980px;
    height: 560px;
    background: var(--card);
  }
  .gold-text {
    background: linear-gradient(100deg, var(--gold-deep), var(--gold-light) 40%, var(--gold-mid) 70%, var(--gold-light));
    -webkit-background-clip: text;
    background-clip: text;
    color: transparent;
  }
  .gold-rule {
    position: absolute;
    background: linear-gradient(180deg, var(--gold-light), var(--gold-mid) 50%, var(--gold-deep));
  }
  .name {
    font-family: "Poppins", sans-serif;
    font-weight: 400;
    letter-spacing: 0.5px;
    white-space: nowrap;
    line-height: 1;
  }
  .name .surname { font-weight: 700; }
  .detail {
    font-family: "Libre Franklin", sans-serif;
    color: var(--silver);
    white-space: nowrap;
    line-height: 1.2;
  }

  /* Front: vertical divider */
  .card--front .gold-rule {
    left: 592px;
    top: 95px;
    width: 3px;
    height: 440px;
  }
  .card--front .identity {
    position: absolute;
    right: 405px;
    top: 245px;
    text-align: right;
  }
  .card--front .name { font-size: 66px; }
  .card--front .phone { font-size: 35px; margin-top: 6px; }
  .card--front .services {
    position: absolute;
    left: 625px;
    top: 232px;
    list-style: none;
    font-size: 34px;
  }

  /* Back: horizontal divider */
  .card--back { text-align: center; }
  .card--back .name {
    position: absolute;
    left: 0; right: 0;
    top: 208px;
    font-size: 64px;
  }
  .card--back .gold-rule {
    left: 38px;
    right: 38px;
    top: 285px;
    height: 4px;
    background: linear-gradient(90deg, var(--gold-deep), var(--gold-light) 45%, var(--gold-mid) 75%, var(--gold-deep));
  }
  .card--back .tagline {
    position: absolute;
    left: 0; right: 0;
    top: 300px;
    font-size: 34px;
    padding-left: 60px;
  }
  .card--back .tagline .sep { margin: 0 6px; }
  .card--back .phone {
    position: absolute;
    left: 0; right: 0;
    top: 348px;
    font-size: 36px;
    padding-left: 0;
  }
</style>
</head>
<body>
  <main class="sheet">
    <section class="card card--front" aria-label="Card front">
      <div class="identity">
        <p class="name gold-text">lana <span class="surname">frost</span></p>
        <p class="detail phone">0491 726 580</p>
      </div>
      <div class="gold-rule"></div>
      <ul class="detail services">
        <li>events</li>
        <li>entertainment</li>
        <li>promotions</li>
      </ul>
    </section>

    <section class="card card--back" aria-label="Card back">
      <p class="name gold-text">lana <span class="surname">frost</span></p>
      <div class="gold-rule"></div>
      <p class="detail tagline">events<span class="sep">·</span>entertainment<span class="sep">·</span>promotions</p>
      <p class="detail phone">0491 726 580</p>
    </section>
  </main>
</body>
</html>
```